Investment website design - investing in mutual funds

I need a design of a website (only homepage for now) dedicated to investment in mutual funds. Attached is a mock up with all the elements the homepage design should contain. The homepage should contain a logo in the upper left corner, the domain the website will run on is www.morvatelsko.cz , in the upper right corner there should be 2 buttons or links SIGN UP / SIGN IN. The bottom of the homepage should contain links to ABOUT US, FAQ, PRIVACY POLICY, CONTACT US.
Now the main elements on the homepage
1) Video that will explain how the investment works exactly, under this video we will have 3 illustrated icons like the ones attached (see 2nd attachement) that will show the potential investor what exactly they could get when investing with us (education for kids, happy life after they retire, regular monthly payment for the rest of their life).
2) On the right side next to the video we will have a calculator where a potential investor can play with the numbers, the investor can fill in the MONTHLY PAYMENT that he wants to invest regularly every month, the time frame of the investment - for how long he wants to invest. Once the potential investor selects those 2 variables we will calculate for him 2 options - either he can get a ONE TIME PAYOUT once he reaches his investment horizon or he can get a regular monthly payment for the rest of his life. Under the laculator there will be a button 'I want to invest ->'. The functionality of the calculator should be similar to the calculator that can be found here http://www.brovikbanka.cz/brovik-podilove-fondy/ and https://pelvaro.cz/.
The design should look similar to https://pelvaro.cz/ (font, colors, logo). We prefer white background in the area where we have the video and calculator. We also like the design of www.truvanex.com. Let me know if you have any questions.

```html
<!DOCTYPE html>
<html lang="en">
<head>
<meta charset="utf-8">
<title>Morvatelsko – Invest in mutual funds</title>
<link rel="stylesheet" href="https://fonts.googleapis.com/css2?family=League+Spartan:wght@500;600;700&family=Roboto:wght@400;500;700&display=swap">
<style>
:root{
  --teal:#45b3bf;
  --orange:#e8573a;
  --black:#111111;
  --ink:#1a1a1a;
  --white:#ffffff;
  --grey-field:#d6d6d6;
  --track:#dcdcdc;
  --video-top:#5aa0b4;
  --video-bottom:#4f8fa3;
  --desk:#a87c4f;
}
*{box-sizing:border-box;margin:0;padding:0}
html,body{width:1200px;height:705px;overflow:hidden;background:var(--white);font-family:"Roboto",Arial,sans-serif;color:var(--ink)}
.page{position:relative;width:1200px;height:705px}

.site-header{position:absolute;left:0;top:0;width:1200px;height:46px;background:var(--teal)}
.brand{position:absolute;left:37px;top:13px;font-family:"Roboto",Arial,sans-serif;font-weight:700;font-size:17px;letter-spacing:.2px;color:var(--black);line-height:20px}
.auth-btn{position:absolute;top:10px;height:26px;display:flex;align-items:center;gap:5px;padding:0 11px;font-size:13px;color:var(--white);text-decoration:none}
.auth-btn svg{width:11px;height:11px;fill:var(--white)}
.sign-in{left:986px;width:77px;background:var(--orange)}
.sign-up{left:1073px;width:82px;background:var(--black)}

.section-title{position:absolute;top:90px;font-family:"League Spartan","Roboto",sans-serif;font-weight:600;font-size:35px;letter-spacing:-1px;line-height:36px;color:var(--black);white-space:nowrap}
.title-video{left:150px}
.title-calc{left:660px}

.video{position:absolute;left:150px;top:155px;width:450px;height:306px;background:linear-gradient(180deg,var(--video-top) 0%,var(--video-bottom) 78%,var(--desk) 80%,#94704a 100%)}
.video .play{position:absolute;left:346px;top:269px}

.benefits{position:absolute;top:480px;left:0;width:100%}
.benefit{position:absolute;width:120px;text-align:center}
.benefit .art{display:block;margin:0 auto;width:106px;height:84px;border:2px solid var(--orange);border-radius:4px}
.benefit .label{display:block;margin-top:6px;font-family:"League Spartan","Roboto",sans-serif;font-weight:500;font-size:13.5px;color:var(--ink)}
.b-edu{left:180px}.b-edu .art{background:linear-gradient(160deg,#ffffff 30%,#e2674a 60%,#f3a72c 100%)}
.b-pass{left:313px}.b-pass .art{background:linear-gradient(160deg,#ffffff 30%,#f3b03a 60%,#3c9bb0 100%)}
.b-ret{left:446px}.b-ret .art{background:linear-gradient(180deg,#ffffff 30%,#e8684c 70%,#2f8c9c 100%)}

.calculator{position:absolute;left:664px;top:154px;width:386px}
.field{display:flex;align-items:center;height:37px;border:2px solid var(--black);padding:0 11px;font-size:11px;color:var(--ink);background:var(--white)}
.field.muted{background:var(--grey-field)}
.slider-label{margin-top:21px;font-size:13px;font-weight:500}
.slider{position:relative;height:14px;margin-top:7px}
.slider .track{position:absolute;left:0;right:0;top:5px;height:4px;background:var(--track)}
.slider .fill{position:absolute;left:0;width:168px;top:5px;height:4px;background:var(--orange)}
.slider .thumb{position:absolute;left:161px;top:0;width:14px;height:14px;border-radius:50%;background:var(--orange)}
.slider .thumb::after{content:"";position:absolute;left:5px;top:4px;width:4px;height:6px;border-left:1.5px solid var(--white);border-right:1.5px solid var(--white)}
.slider-range{display:flex;justify-content:space-between;margin-top:1px;font-size:12px}
.slider-range .min{font-weight:700}
.payout{margin-top:9px}
.or{text-align:center;font-size:12px;height:31px;line-height:31px}
.invest-btn{display:flex;align-items:center;justify-content:center;gap:7px;margin:28px 0 0 2px;width:382px;height:46px;background:var(--orange);color:var(--white);font-weight:700;font-size:17px;text-decoration:none}
.invest-btn svg{width:14px;height:14px}

.site-footer{position:absolute;left:0;top:635px;width:1200px;height:70px;background:var(--black);color:var(--white);text-align:center}
.footer-nav{margin-top:18px;font-size:13px}
.footer-nav a{color:var(--white);text-decoration:none}
.footer-nav .sep{margin:0 6px}
.copyright{margin-top:6px;font-size:9.5px}
</style>
</head>
<body>
<div class="page">
  <header class="site-header">
    <div class="brand">MORVATELSKO</div>
    <a class="auth-btn sign-in" href="#"><svg viewBox="0 0 12 12"><circle cx="6" cy="3.2" r="2.7"/><path d="M0.8 12c0-3.4 2.3-5.3 5.2-5.3s5.2 1.9 5.2 5.3z"/></svg>Sign in</a>
    <a class="auth-btn sign-up" href="#"><svg viewBox="0 0 12 12"><path d="M1 2h6v1.3H2.3v7.4h7.4V6H11v6H1z"/><path d="M9.6 0.6l1.8 1.8-5 5-2.3.5.5-2.3z"/></svg>Sign up</a>
  </header>

  <h2 class="section-title title-video">VIDEO ABOUT OUR PRODUCT</h2>
  <h2 class="section-title title-calc">OUR ONLINE CALCULATOR</h2>

  <div class="video" role="img" aria-label="Explainer video still: cartoon man at an office desk with a computer">
    <svg class="play" width="66" height="66" viewBox="0 0 66 66" style="left:196px;top:114px"><circle cx="33" cy="33" r="29" fill="none" stroke="#fff" stroke-width="5"/><path d="M25 19l22 14-22 14z" fill="#fff"/></svg>
  </div>

  <div class="benefits">
    <div class="benefit b-edu"><span class="art" role="img" aria-label="Illustration of stacked books with a graduation cap"></span><span class="label">Education for kids</span></div>
    <div class="benefit b-pass"><span class="art" role="img" aria-label="Illustration of a person relaxing on a bean bag"></span><span class="label">Passive income</span></div>
    <div class="benefit b-ret"><span class="art" role="img" aria-label="Illustration of a retiree playing golf"></span><span class="label">Happy retirement</span></div>
  </div>

  <form class="calculator">
    <div class="field">Regular monthly investment</div>
    <div class="slider-label">Length of investment</div>
    <div class="slider"><span class="track"></span><span class="fill"></span><span class="thumb"></span></div>
    <div class="slider-range"><span class="min">0</span><span>30 years</span></div>
    <div class="field payout">One time payout:</div>
    <div class="or">OR</div>
    <div class="field muted">Monthly payment:</div>
    <a class="invest-btn" href="#">I WANT TO INVEST <svg viewBox="0 0 14 14"><circle cx="7" cy="7" r="7" fill="#fff"/><path d="M5.5 3.8L8.7 7 5.5 10.2" fill="none" stroke="#e8573a" stroke-width="2"/></svg></a>
  </form>

  <footer class="site-footer">
    <nav class="footer-nav"><a href="#">About Us</a><span class="sep">|</span><a href="#">FAQ</a><span class="sep">|</span><a href="#">Privacy policy</a><span class="sep">|</span><a href="#">Contact</a></nav>
    <div class="copyright">© 2017 morvatelsko . All rights reserved.</div>
  </footer>
</div>
</body>
</html>
```